"Velmora Kestrel Bridgeworks": unique end to end Chinese marketing and ecommerce solutions*

I would like to create a company website for my trademark: "Velmora Kestrel Bridgeworks". We are based in Iceland. We are the only company in the market offering end-to-end Chinese digital marketing and eCommerce solutions. We help companies grow their brands and sales towards Chinese - whether tourism, export of products or services.
I include the logo that we have come up with in terms of colours and fonts.
The font is Trajan - I would like to use normal letters (capital and lowercase) for text.
Front page: Picture with colour filter. Logo in white. Text line underneath.
I am inspired by this website:
https://www.pelorumgrove.example/
I like these short videos for landing page:
https://www.framelodex.example/video/clip-30417852-ridge-scenic-vista-mountains
https://www.framelodex.example/video/clip-2093847155-4k-aerial-video-ridge-path-vista
https://www.framelodex.example/video/clip-3058172649-ridge-path-vista
Icelandic businesses looking for business opportunities in China or to attract Chinese tourists.
Digital Marketing

```html
<!DOCTYPE html>
<html lang="en">
<head>
<meta charset="utf-8">
<title>Velmora Kestrel Bridgeworks</title>
<link href="https://fonts.googleapis.com/css2?family=Cinzel:wght@400;600&display=swap" rel="stylesheet">
<style>
:root{
  --page:#f6f6f9;
  --ink:#3d3d45;
  --ink-soft:#5e5e68;
  --gold:#c89a5e;
  --gold-light:#e3c79c;
  --blue:#1f5fa8;
  --navy:#173d6e;
  --white:#ffffff;
  --line:#d9c3a2;
  --band:#efe9e2;
}
*{box-sizing:border-box;margin:0;padding:0}
html,body{width:1200px;height:3496px;overflow:hidden;background:var(--page)}
body{font-family:"Cinzel",serif;color:var(--ink)}
.canvas{position:relative;width:1200px;height:3496px;overflow:hidden;background:var(--page)}
.abs{position:absolute}
.hero{left:0;top:0;width:1200px;height:900px}
.hero svg{position:absolute;left:0;top:0}
.nav{left:0;top:88px;width:1200px;font-size:15px;letter-spacing:1px;color:var(--white)}
.nav a{position:absolute;color:var(--white);text-decoration:none}
.brand{left:450px;top:60px;width:300px;text-align:center;color:var(--white)}
.brand .mark{width:34px;height:34px;border-radius:50%;background:var(--white);opacity:.9;margin:0 auto 10px}
.brand .name{font-size:22px;font-weight:600;letter-spacing:1px;line-height:1.2}
.hero-title{left:0;top:360px;width:1200px;text-align:center;color:var(--white);font-size:64px;line-height:1.05;font-weight:400;text-shadow:0 2px 8px rgba(0,0,0,.35)}
.hero-text{left:300px;top:540px;width:600px;text-align:center;color:var(--white);font-size:14px;line-height:1.4}
.btn{display:inline-block;border:2px solid var(--gold);border-radius:20px;padding:8px 34px;font-size:16px;color:var(--ink);background:var(--white);font-family:"Cinzel",serif}
.btn.light{background:transparent;color:var(--white);border-color:var(--gold-light)}
.hero-btn{left:530px;top:624px;width:140px;text-align:center;padding:6px 0}
.section-title{font-size:28px;font-weight:400;letter-spacing:2px;color:var(--ink)}
.body-text{font-size:14px;line-height:1.55;color:var(--ink-soft)}
.intro{left:160px;top:690px;width:880px;text-align:center}
.intro .body-text{margin:18px 0 24px}
.band{left:0;top:1020px;width:760px;height:250px;background:var(--band)}
.band-text{left:100px;top:1060px;width:360px}
.band-text h2{font-size:34px;font-weight:400;line-height:1.1;color:var(--ink);margin-bottom:14px}
.illustration{left:660px;top:905px;width:460px;height:410px;border-radius:48% 52% 44% 56%/50% 40% 60% 50%;background:linear-gradient(135deg,#e7e4fb,#c9c4f2 60%,#f0dcc8)}
.feature{width:560px}
.feature .body-text{margin:16px 0 20px}
.blob{border-radius:55% 45% 50% 50%/45% 55% 45% 55%}
.blob-1{left:140px;top:1360px;width:330px;height:250px;background:linear-gradient(135deg,#f2dcc8,#c9a48a 60%,#e6c0a6)}
.blob-2{left:760px;top:1660px;width:300px;height:300px;background:linear-gradient(135deg,#b3c6d6,#6d8aa3 55%,#e9e1d4);border-radius:50% 45% 55% 50%}
.blob-3{left:130px;top:1980px;width:330px;height:310px;background:linear-gradient(135deg,#d7dde6,#8d9db3 55%,#f2c9c0);border-radius:48% 52% 40% 60%/55% 45% 55% 45%}
.blog-title{left:0;top:2322px;width:1200px;text-align:center;font-size:32px}
.card{top:2410px;width:240px}
.card .photo{width:240px;height:155px}
.card .body-text{font-size:12px;line-height:1.4;text-align:center;margin:18px 0 20px}
.card .btn{display:block;width:150px;margin:0 auto;text-align:center;padding:5px 0;font-size:14px}
.booking{left:70px;top:2840px;width:520px}
.booking h2{font-size:24px;font-weight:400;margin-bottom:18px}
.form{left:720px;top:2840px;width:360px}
.field{display:block;width:360px;height:40px;border:1px solid var(--line);background:var(--white);margin-bottom:14px;font-family:"Cinzel",serif;font-size:13px;padding:10px 12px;color:#999}
.field.area{height:100px}
.submit{display:inline-block;background:var(--gold);color:var(--white);font-size:12px;padding:8px 18px}
.footer{left:0;top:3090px;width:1200px;height:406px}
.footer svg{position:absolute;left:0;top:0}
.foot-brand{left:70px;top:3200px;width:280px;text-align:center;color:var(--white)}
.foot-brand .mark{width:30px;height:30px;border-radius:50%;background:var(--white);margin:0 auto 10px;opacity:.9}
.foot-brand .name{font-size:20px;font-weight:600;line-height:1.2}
.foot-brand p{font-size:10px;line-height:1.5;margin-top:30px;text-align:left}
.foot-col{top:3225px;color:var(--white)}
.foot-col h3{font-size:13px;font-weight:600;margin-bottom:10px}
.foot-col li{list-style:none;font-size:11px;line-height:1.75}
.foot-col p{font-size:11px;line-height:1.5}
.news{margin-top:14px;display:flex}
.news span{display:block;width:140px;height:26px;background:var(--white);font-size:10px;color:#999;padding:6px 8px}
.news b{display:block;background:var(--gold);font-size:10px;font-weight:400;padding:7px 10px}
.social{display:flex;align-items:center;gap:10px;margin-top:22px;font-size:11px}
.social i{display:block;width:20px;height:20px;border-radius:50%;border:2px solid var(--white)}
.copyright{left:0;top:3462px;width:1200px;text-align:center;font-size:10px;color:var(--white);letter-spacing:1px}
</style>
</head>
<body>
<div class="canvas">

  <!-- Hero -->
  <div class="abs hero">
    <svg width="1200" height="900" viewBox="0 0 1200 900">
      <defs>
        <linearGradient id="heroTone" x1="0" y1="0" x2="0" y2="1">
          <stop offset="0" stop-color="#9bb3c4"/>
          <stop offset=".35" stop-color="#6c8a6a"/>
          <stop offset=".7" stop-color="#4f6a3c"/>
          <stop offset="1" stop-color="#8a7a5c"/>
        </linearGradient>
      </defs>
      <path role="img" aria-label="Photo of a mountain ridge with an ancient stone wall under a soft colour filter" d="M0 0H1200V700C1050 780 900 640 720 680C560 715 420 600 260 640C150 668 70 720 0 690Z" fill="url(#heroTone)"/>
      <path d="M0 690C70 720 150 668 260 640C420 600 560 715 720 680C900 640 1050 780 1200 700V900H0Z" fill="#f6f6f9"/>
    </svg>
  </div>

  <nav class="abs nav">
    <a style="left:145px">Home</a>
    <a style="left:245px">About</a>
    <a style="left:340px">Tourism</a>
    <a style="left:780px">Strategies</a>
    <a style="left:885px">Platforms</a>
    <a style="left:980px">Contact</a>
  </nav>

  <div class="abs brand">
    <div class="mark"></div>
    <div class="name">Velmora Kestrel Bridgeworks</div>
  </div>

  <h1 class="abs hero-title">Reach Your Potential<br>Chinese Customers.</h1>
  <p class="abs hero-text">Lorem ipsum dolor sit amet, consectetur adipiscing elit, sed do eiusmod tempor incididunt ut labore et dolore magna aliqua ut enim ad minim.</p>
  <span class="abs btn light hero-btn">Explore</span>

  <!-- Intro -->
  <div class="abs intro">
    <h2 class="section-title">Lorem Ipsum Dolor</h2>
    <p class="body-text">Lorem ipsum dolor sit amet, consectetur adipiscing elit, sed do eiusmod tempor incididunt ut labore et dolore magna aliqua. Ut enim ad minim veniam, quis nostrud exercitation ullamco laboris nisi ut aliquip ex ea commodo consequat.</p>
    <span class="btn">Read More</span>
  </div>

  <!-- Getting down to business -->
  <div class="abs band"></div>
  <div class="abs illustration" role="img" aria-label="Illustration of a team working around a large analytics screen"></div>
  <div class="abs band-text">
    <h2>Getting Down<br>To Business</h2>
    <p class="body-text">Lorem ipsum dolor sit amet, consectetur adipiscing elit, sed do eiusmod tempor incididunt ut labore et dolore magna aliqua.</p>
  </div>

  <!-- Features -->
  <div class="abs blob blob-1" role="img" aria-label="Photo of a handshake"></div>
  <div class="abs feature" style="left:540px;top:1430px">
    <h2 class="section-title">Lorem Ipsum Dolor</h2>
    <p class="body-text">Lorem ipsum dolor sit amet, consectetur adipiscing elit, sed do eiusmod tempor incididunt ut labore et dolore magna aliqua. Ut enim ad minim veniam, quis nostrud exercitation ullamco laboris nisi ut aliquip ex ea commodo consequat.</p>
    <span class="btn" style="font-size:14px;padding:5px 28px">Read More</span>
  </div>

  <div class="abs blob blob-2" role="img" aria-label="Photo of a phone showing social media apps"></div>
  <div class="abs feature" style="left:160px;top:1740px;text-align:center">
    <h2 class="section-title">Lorem Ipsum Dolor</h2>
    <p class="body-text">Lorem ipsum dolor sit amet, consectetur adipiscing elit, sed do eiusmod tempor incididunt ut labore et dolore magna aliqua. Ut enim ad minim veniam, quis nostrud exercitation ullamco laboris nisi ut aliquip ex ea commodo consequat.</p>
    <span class="btn" style="font-size:14px;padding:5px 28px">Read More</span>
  </div>

  <div class="abs blob blob-3" role="img" aria-label="Photo of hands typing on a laptop"></div>
  <div class="abs feature" style="left:540px;top:2035px">
    <h2 class="section-title">Lorem Ipsum Dolor</h2>
    <p class="body-text">Lorem ipsum dolor sit amet, consectetur adipiscing elit, sed do eiusmod tempor incididunt ut labore et dolore magna aliqua. Ut enim ad minim veniam, quis nostrud exercitation ullamco laboris nisi ut aliquip ex ea commodo consequat.</p>
    <span class="btn" style="font-size:14px;padding:5px 28px">Read More</span>
  </div>

  <!-- Blog -->
  <h2 class="abs section-title blog-title">Blog</h2>

  <div class="abs card" style="left:70px">
    <div class="photo" role="img" aria-label="Photo of a waterfall landscape" style="background:linear-gradient(160deg,#cfe0ec,#8aa59a 55%,#4e6b52)"></div>
    <p class="body-text">Lorem ipsum dolor sit amet, consectetur adipiscing elit sed do eiusmod tempor incididunt ut labore et dolore magna aliqua.</p>
    <span class="btn">Read More</span>
  </div>
  <div class="abs card" style="left:340px">
    <div class="photo" role="img" aria-label="Photo of a city skyline at dusk" style="background:linear-gradient(160deg,#4a6fa5,#2c3f66 55%,#c98b5a)"></div>
    <p class="body-text">Lorem ipsum dolor sit amet, consectetur adipiscing elit sed do eiusmod tempor incididunt ut labore et dolore magna aliqua.</p>
    <span class="btn">Read More</span>
  </div>
  <div class="abs card" style="left:610px">
    <div class="photo" role="img" aria-label="Photo of people working at a desk with charts" style="background:linear-gradient(160deg,#e8e4df,#b6aea6 55%,#7d8894)"></div>
    <p class="body-text">Lorem ipsum dolor sit amet, consectetur adipiscing elit sed do eiusmod tempor incididunt ut labore et dolore magna aliqua.</p>
    <span class="btn">Read More</span>
  </div>
  <div class="abs card" style="left:880px">
    <div class="photo" role="img" aria-label="Photo of a megaphone on a blue background" style="background:linear-gradient(160deg,#8fc4ec,#4b97d6 60%,#d9ecf8)"></div>
    <p class="body-text">Lorem ipsum dolor sit amet, consectetur adipiscing elit sed do eiusmod tempor incididunt ut labore et dolore magna aliqua.</p>
    <span class="btn">Read More</span>
  </div>

  <!-- Booking -->
  <div class="abs booking">
    <h2>Book an Appointment</h2>
    <p class="body-text">Lorem ipsum dolor sit amet, consectetur adipiscing elit, sed do eiusmod tempor incididunt ut labore et dolore magna aliqua. Ut enim ad minim veniam, quis nostrud exercitation ullamco laboris nisi ut aliquip ex ea commodo consequat.</p>
  </div>
  <div class="abs form">
    <span class="field">Name</span>
    <span class="field">Email</span>
    <span class="field area">Message</span>
    <span class="submit">Submit</span>
  </div>

  <!-- Footer -->
  <div class="abs footer">
    <svg width="1200" height="406" viewBox="0 0 1200 406">
      <defs>
        <linearGradient id="footTone" x1="0" y1="0" x2="1" y2="0">
          <stop offset="0" stop-color="#c89a5e"/>
          <stop offset=".45" stop-color="#8a8a7e"/>
          <stop offset=".7" stop-color="#2f62a3"/>
          <stop offset="1" stop-color="#173d6e"/>
        </linearGradient>
      </defs>
      <path d="M0 40C200 0 380 70 600 50C820 30 1000 -10 1200 30V406H0Z" fill="url(#footTone)"/>
      <rect x="0" y="360" width="1200" height="46" fill="#1a3f6e" opacity=".35"/>
    </svg>
  </div>

  <div class="abs foot-brand">
    <div class="mark"></div>
    <div class="name">Velmora Kestrel Bridgeworks</div>
    <p>Lorem ipsum dolor sit amet, consectetur adipiscing elit, sed do eiusmod tempor incididunt ut labore et dolore magna aliqua ut enim ad minim veniam quis nostrud.</p>
  </div>

  <div class="abs foot-col" style="left:460px">
    <h3>Company Info</h3>
    <ul><li>About Us</li><li>Contact Us</li><li>Blog</li><li>Privacy Policy</li><li>Terms &amp; Conditions</li></ul>
  </div>
  <div class="abs foot-col" style="left:660px">
    <h3>Services</h3>
    <ul><li>Tourism</li><li>Marketing</li><li>Strategies</li><li>Platforms</li></ul>
  </div>
  <div class="abs foot-col" style="left:880px;width:260px">
    <h3>Keep in Touch</h3>
    <p>Lorem ipsum dolor sit amet, consectetur adipiscing elit sed do eiusmod tempor incididunt ut labore et dolore magna aliqua.</p>
    <div class="news"><span>Email</span><b>Subscribe</b></div>
    <div class="social">Follow us <i></i><i></i><i></i><i></i><i></i></div>
  </div>

  <p class="abs copyright">© 2020 Velmora Kestrel Bridgeworks. All Rights Reserved.</p>
</div>
</body>
</html>
```